Tarrendale Secondary College House displays

Our school has 4 new houses that are designed to promote school connectedness and school pride. Each house display should include the name of the house, a silhouette portrait of the person the house is named after and a famous quote from that person. Each house display should also promote the unique house colour. Details are included in the attached word document. I have also attached a Marcus Threlby poster that gives some sort of idea about the look and feel we are after. The house name should be quite prominent.

Target Market(s)

Tarrendale Secondary College has 1800 students. We are a unique school committed to a strengths based program. Our house system is designed to connect students to each other and to the school. To understand our school visit our website at www.tarrendalesc.vic.edu.au

Logo Text

We want a logo for each of our houses that has the house name on it - see the attached word document for details.

Font styles to use
Sans Serif

Colors
0792cd
00a990
fbed22
ec1f27

Requirements
Must have
• Colour- each house must include the colour it is aligned to. This is outlined in the attached word document

```html
<!DOCTYPE html>
<html lang="en">
<head>
<meta charset="utf-8">
<title>Tarrendale Secondary College – House Displays</title>
<link href="https://fonts.googleapis.com/css2?family=Lato:ital,wght@0,300;0,400;0,700;0,900;1,400&display=swap" rel="stylesheet">
<style>
  :root {
    --teal: #00a990;
    --red: #ec1f27;
    --yellow: #fbed22;
    --blue: #0792cd;
    --ink: #1a1a1a;
    --white: #ffffff;
    --page: #ffffff;
  }
  * { margin: 0; padding: 0; box-sizing: border-box; }
  html, body { width: 1200px; height: 1200px; overflow: hidden; background: var(--page); }
  body { position: relative; font-family: 'Lato', sans-serif; color: var(--ink); }

  .house-poster {
    position: absolute; top: 80px; width: 266px; height: 533px; overflow: hidden;
    background: var(--house);
  }
  .house-poster--harlow { left: 46px; --house: var(--teal); --deep: #00604f; --bio: #0d3b33; }
  .house-poster--ashby { left: 326px; --house: var(--red); --deep: #7a0c10; --bio: #4a0a0c; }
  .house-poster--koriba { left: 606px; --house: var(--yellow); --deep: #6f6a0c; --bio: #2b2a08; }
  .house-poster--strand { left: 886px; --house: var(--blue); --deep: #0b2f63; --bio: #0b2f63; }

  .poster-head {
    position: absolute; left: 0; top: 0; width: 100%; height: 275px;
    background:
      radial-gradient(ellipse at 20% 85%, rgba(0,0,0,.16), transparent 55%),
      radial-gradient(ellipse at 80% 10%, rgba(0,0,0,.10), transparent 50%),
      linear-gradient(180deg, rgba(0,0,0,.04), rgba(0,0,0,.14)),
      var(--house);
  }
  .house-name {
    position: absolute; right: 38px; font-weight: 900; color: var(--white);
    font-size: 60px; line-height: 60px; letter-spacing: -0.5px;
  }
  .house-quote {
    position: absolute; right: 38px; text-align: right;
    font-size: 16px; line-height: 19.2px; font-weight: 400; color: var(--ink);
  }
  .quote-mark {
    font-weight: 900; font-size: 30px; color: var(--deep);
    line-height: 0; vertical-align: -6px; letter-spacing: -2px;
  }
  .quote-mark--open { margin-right: 2px; }
  .quote-mark--close { margin-left: 3px; }

  .poster-body { position: absolute; left: 0; top: 275px; width: 100%; height: 258px; }
  .portrait {
    position: absolute; right: 0; bottom: 0; width: 136px; height: 221px;
    background:
      radial-gradient(ellipse at 55% 40%, var(--deep) 0%, var(--deep) 50%, transparent 72%),
      linear-gradient(180deg, transparent 55%, var(--deep) 100%);
  }
  .bio {
    position: absolute; left: 23px; width: 92px;
    font-size: 9.4px; line-height: 11.6px; font-weight: 300; color: var(--bio);
  }
  .bio strong { font-weight: 700; display: block; color: var(--ink); }
  .house-poster--strand .bio strong { color: var(--bio); }
  .bio .years { display: block; margin-top: 6px; font-weight: 400; font-size: 9.6px; color: var(--ink); }
  .house-poster--strand .bio .years { color: var(--bio); }

  .feature-panel {
    position: absolute; left: 0; top: 744px; width: 808px; height: 456px; background: var(--red);
  }
  .feature-portrait { position: absolute; }
  .feature-portrait--left {
    left: 0; top: 648px; width: 416px; height: 552px;
    background: radial-gradient(ellipse at 45% 50%, rgba(60,10,10,.85) 0%, rgba(90,15,15,.6) 50%, transparent 75%);
  }
  .feature-portrait--right {
    left: 808px; top: 696px; width: 392px; height: 504px;
    background: radial-gradient(ellipse at 60% 55%, #3a3a3a 0%, #555 40%, rgba(255,255,255,0) 75%);
  }
  .design-notes {
    position: absolute; left: 358px; top: 850px; width: 460px; text-align: center;
    font-weight: 300; font-size: 30px; line-height: 30px; color: var(--ink); letter-spacing: .3px;
  }
  .design-notes p + p { margin-top: 36px; }
</style>
</head>
<body>

<section class="house-poster house-poster--harlow">
  <div class="poster-head">
    <h2 class="house-name" style="top:56px;">Harlow</h2>
    <p class="house-quote" style="top:120px;"><span class="quote-mark quote-mark--open">“</span>As a young girl I would<br>watch the clouds roll by. I<br>hoped one day I could rise<br>above the dusty paddocks<br>and the tall river gums to<br>chase the storms beyond<br>the far horizon line.<span class="quote-mark quote-mark--close">”</span></p>
  </div>
  <div class="poster-body">
    <div class="portrait" role="img" aria-label="Halftone portrait of Nora-Wren Harlow in flying cap and goggles"></div>
    <p class="bio" style="top:69px;"><strong>Nora-Wren Harlow:</strong>a trailblazing coastal pilot, known as "The Flying Teacher", and the founder and patron of the Southern Women Aviators' Guild.<span class="years">1921-2004</span></p>
  </div>
</section>

<section class="house-poster house-poster--ashby">
  <div class="poster-head">
    <h2 class="house-name" style="top:82px;">Ashby</h2>
    <p class="house-quote" style="top:146px;"><span class="quote-mark quote-mark--open">“</span>Small steps<br>still travel far.<br>Brave hearts<br>open closed doors.<span class="quote-mark quote-mark--close">”</span></p>
  </div>
  <div class="poster-body">
    <div class="portrait" role="img" aria-label="Halftone portrait of Tessa Ashby"></div>
    <p class="bio" style="top:49px; left:17px;"><strong>Tessa Ashby:</strong>a pioneering educator and author who opened free reading rooms for young learners across the region.<span class="years">1880-1951</span></p>
  </div>
</section>

<section class="house-poster house-poster--koriba">
  <div class="poster-head">
    <h2 class="house-name" style="top:74px;">Koriba</h2>
    <p class="house-quote" style="top:138px;"><span class="quote-mark quote-mark--open">“</span>I sat by the shore thinking<br>about our people.<br>How strong we could<br>be, long after<br>I have gone.<span class="quote-mark quote-mark--close">”</span></p>
  </div>
  <div class="poster-body">
    <div class="portrait" role="img" aria-label="Halftone portrait of Elias Koriba"></div>
    <p class="bio" style="top:62px; left:20px;"><strong>Elias Koriba:</strong>known for his work campaigning for community land rights and for leading a landmark case which reshaped how the law saw <em>traditional ownership</em>.<span class="years">1940-1998</span></p>
  </div>
</section>

<section class="house-poster house-poster--strand">
  <div class="poster-head">
    <h2 class="house-name" style="top:20px; right:34px;">Strand</h2>
    <p class="house-quote" style="top:84px;"><span class="quote-mark quote-mark--open">“</span>I love a challenge. There’s<br>always a new hill to<br>climb, new friends<br>to make... You’ve just<br>got to find your spark<br>and chase it hard. That’s<br>where the joy is,<br>that’s how you find<br>your own true path.<span class="quote-mark quote-mark--close">”</span></p>
  </div>
  <div class="poster-body">
    <div class="portrait" role="img" aria-label="Halftone portrait of Jack Strand smiling"></div>
    <p class="bio" style="top:34px; left:17px;"><strong>Jack Strand:</strong>one of SFL’s best-loved players who won the Ridgeway Medal in 1994. Off the field, he was a respected mentor, philanthropist, charity worker and writer.<span class="years">1970-2015</span></p>
  </div>
</section>

<div class="feature-panel"></div>
<div class="feature-portrait feature-portrait--left" role="img" aria-label="Enlarged halftone screen portrait of Tessa Ashby"></div>
<div class="feature-portrait feature-portrait--right" role="img" aria-label="Enlarged black halftone screen portrait of Jack Strand"></div>

<div class="design-notes">
  <p>Lato font family</p>
  <p>Screen treatment of<br>images to give uniform feel</p>
  <p>Grunge treatment<br>of main text area<br>for continuity</p>
</div>

</body>
</html>
```